Breakfast Briefings / Lunch & Learn

I would like to have a double sided flyer size 8x10 to display the breakfast briefing on one side and Lunch & Learn on the other side.

Header on each side to say
2018 Calendar Breakfast Briefing (on the breakfast side)
2018 Calendar Lunch & Learn (on the lunch side)

I have attached a copy of the files we would like to use.

Learn

```html
<!DOCTYPE html>
<html lang="en">
<head>
<meta charset="utf-8">
<title>2018 Calendar Breakfast Briefing – Schedule</title>
<link href="https://fonts.googleapis.com/css2?family=Jost:wght@400;500&family=Open+Sans:wght@700&family=Lato:wght@400;700&display=swap" rel="stylesheet">
<style>
  :root {
    --paper: #f7f7f8;
    --band: #3a3a3b;
    --ink: #333333;
    --accent: #1ba6e2;
    --white: #ffffff;
    --logo-grey: #b9b9b9;
  }
  * { margin: 0; padding: 0; box-sizing: border-box; }
  html, body { width: 960px; height: 1200px; overflow: hidden; background: var(--paper); }
  .flyer { position: relative; width: 960px; height: 1200px; background: var(--paper); font-family: "Lato", sans-serif; color: var(--ink); }
  .hero { position: absolute; left: 0; top: 0; width: 960px; height: 540px; }
  .brand { position: absolute; left: 498px; top: 72px; display: flex; align-items: center; gap: 12px;
    font-family: "Jost", sans-serif; font-weight: 400; font-size: 34px; letter-spacing: 6px; color: var(--logo-grey); }
  .brand-mark { width: 16px; height: 16px; background: var(--accent); }
  .title { position: absolute; left: 498px; top: 168px; font-family: "Jost", sans-serif; font-weight: 500;
    font-size: 40px; line-height: 48px; color: var(--white); letter-spacing: 0.5px; }
  .schedule-heading { position: absolute; right: 48px; top: 448px; font-family: "Jost", sans-serif; font-weight: 500;
    font-size: 57px; color: var(--accent); letter-spacing: 1px; }
  .quarter { position: absolute; left: 0; width: 960px; }
  .months, .entries { display: grid; grid-template-columns: 229px 230px 230px 231px; padding-left: 26px; }
  .months { height: 42px; background: var(--band); align-items: center; text-align: center;
    font-family: "Open Sans", sans-serif; color: var(--white); font-weight: 700; font-size: 21px; letter-spacing: -0.2px; }
  .entries { text-align: center; padding-top: 16px; }
  .dept { font-weight: 700; font-size: 25px; line-height: 34px; }
  .speaker { font-size: 24px; line-height: 26px; margin-top: 6px; }
  .speaker .late { display: inline-block; margin-top: 10px; }
  .q1 { top: 570px; }
  .q2 { top: 806px; }
  .q3 { top: 1024px; }
  .q3 .months { height: 46px; }
</style>
</head>
<body>
<main class="flyer">
  <svg class="hero" viewBox="0 0 960 540">
    <defs>
      <linearGradient id="panelShade" x1="0" y1="0" x2="1" y2="0.3">
        <stop offset="0" stop-color="#141414"/>
        <stop offset="0.6" stop-color="#3a3a3a"/>
        <stop offset="1" stop-color="#9a9a9a"/>
      </linearGradient>
      <linearGradient id="photoTone" x1="0" y1="0" x2="1" y2="0.2">
        <stop offset="0" stop-color="#dcdcdc"/>
        <stop offset="0.42" stop-color="#cfcbc8"/>
        <stop offset="0.55" stop-color="#3d2417"/>
        <stop offset="1" stop-color="#1e100a"/>
      </linearGradient>
      <linearGradient id="edgeShadow" x1="0" y1="0" x2="0" y2="1">
        <stop offset="0" stop-color="#8d8d8d"/>
        <stop offset="1" stop-color="#d5d5d5"/>
      </linearGradient>
    </defs>
    <path d="M0,0 H960 V252 Q640,460 0,530 Z" fill="url(#edgeShadow)"/>
    <path d="M0,0 H960 V244 Q640,448 0,516 Z" fill="url(#panelShade)"/>
    <path d="M0,0 H640 L840,330 Q520,440 0,508 Z" fill="url(#photoTone)" role="img" aria-label="Photo: overhead view of a cup of black coffee, a croissant on a white plate and a laptop on a marble table"/>
  </svg>

  <div class="brand"><span class="brand-mark"></span>veltra</div>
  <h1 class="title">2018 CALENDAR<br>BREAKFAST BRIEFING</h1>
  <h2 class="schedule-heading">SCHEDULE</h2>

  <section class="quarter q1">
    <div class="months"><span>JANUARY</span><span>FEBRUARY</span><span>MARCH</span><span>APRIL</span></div>
    <div class="entries">
      <div><p class="dept">MEDICAL</p><p class="speaker">Samuel Okafor<br>2019<br>TBD</p></div>
      <div><p class="dept">SALES</p><p class="speaker">Leo Marchetti<br>2019<br><span class="late">TBD</span></p></div>
      <div><p class="dept">FINANCE</p><p class="speaker">Tomás Reyes</p></div>
      <div><p class="dept">R &amp; D</p><p class="speaker">Hannah Lindqvist</p></div>
    </div>
  </section>

  <section class="quarter q2">
    <div class="months"><span>MAY</span><span>JUNE</span><span>JULY</span><span>AUGUST</span></div>
    <div class="entries">
      <div><p class="dept">OPERATIONS</p><p class="speaker">Oliver Brandt</p></div>
      <div><p class="dept">CLINICAL / REG</p><p class="speaker">Ines Moreau</p></div>
      <div><p class="dept">QUALITY</p><p class="speaker">Marcus Whitfield</p></div>
      <div><p class="dept">PEOPLE</p><p class="speaker">Elena Novak</p></div>
    </div>
  </section>

  <section class="quarter q3">
    <div class="months"><span>SEPTEMBER</span><span>OCTOBER</span><span>NOVEMBER</span><span>DECEMBER</span></div>
    <div class="entries">
      <div><p class="dept">MARKETING</p><p class="speaker">Gavin Holloway</p></div>
      <div><p class="dept">LEGAL</p><p class="speaker">Felix Ortega</p></div>
      <div><p class="dept">MARKET ACCESS</p><p class="speaker">Rebecca Haldane</p></div>
      <div><p class="dept">TOS</p><p class="speaker">Nora Bishop</p></div>
    </div>
  </section>
</main>
</body>
</html>
```